Flyer design for guitar parts website

We are looking for an eye catching flyer design to include within our order packaging to persuade our Zubit and Kestrix customers to purchase from our website.

The flyer will be double sided, with one side offering buyers a discount for shopping on our website, and the other side advertising our loyalty points scheme, and the benefits the company it.

We've attached our company logo and our loyalty points logo.

I've also attached a banner design we used recently for our rewards program.

Target Market(s)

Males, aged 20 to 65

Colors
f68e4d
f04a51
886aae
3377b5

Requirements
Must have
• The flyer will be A6 size
• The focus of the front must be on the 20% discount for first order.
• The web address must also be prominent, as must our logo
• There will also be a discount code displayed.
• The back fo the flyer will contain the loyalyt points logo, and information about how the points work, and how they can be redeemed

```html
<!DOCTYPE html>
<html lang="en">
<head>
<meta charset="utf-8">
<title>Ridgeline Guitars – First Order Discount Flyer</title>
<link rel="stylesheet" href="https://fonts.googleapis.com/css2?family=Open+Sans:wght@400;700&display=swap">
<style>
  :root {
    --orange: #f18a50;
    --orange-deep: #e64f2c;
    --red: #e5302d;
    --peach: #f9b98e;
    --peach-light: #fac09a;
    --ink: #1a1512;
    --white: #ffffff;
    --photo-dark: #3f2520;
    --photo-mid: #7a4a38;
    --photo-warm: #b07452;
  }
  * { margin: 0; padding: 0; box-sizing: border-box; }
  html, body { width: 851px; height: 1200px; overflow: hidden; background: var(--orange); }
  .flyer {
    position: relative;
    width: 851px;
    height: 1200px;
    overflow: hidden;
    background: var(--orange);
    font-family: "Open Sans", Arial, sans-serif;
  }
  .backdrop { position: absolute; inset: 0; }
  .brand {
    position: absolute;
    left: 24px;
    top: 50px;
    display: flex;
    align-items: center;
    gap: 12px;
    font-weight: 700;
    font-size: 48px;
    line-height: 1;
    color: var(--red);
  }
  .brand-dot {
    width: 22px; height: 22px;
    border-radius: 50%;
    background: var(--red);
  }
  .offer-frame {
    position: absolute;
    left: 49px; top: 359px;
    width: 673px; height: 692px;
    border: 1.5px solid var(--white);
  }
  .tag-backing {
    position: absolute;
    left: 60px; top: 626px;
    width: 619px; height: 266px;
    background: var(--peach-light);
    transform: rotate(-5.8deg);
    transform-origin: left top;
  }
  .tag {
    position: absolute;
    left: 71px; top: 650px;
    width: 604px; height: 248px;
    background: var(--red);
    transform: rotate(-8.5deg);
    transform-origin: left top;
  }
  .tag-hole {
    position: absolute;
    left: 629px; top: 537px;
    width: 42px; height: 42px;
    border-radius: 50%;
    background: var(--orange);
  }
  .tag-lead,
  .tag-value {
    position: absolute;
    line-height: 1;
    white-space: nowrap;
  }
  .tag-lead {
    left: 47px; top: 48px;
    font-size: 46px;
    color: var(--ink);
  }
  .tag-value {
    left: 56px; top: 130px;
    font-size: 76px;
    color: var(--white);
  }
  .code-wash {
    position: absolute;
    left: 115px; top: 954px;
    width: 532px; height: 73px;
    border-radius: 14px;
    background: var(--peach);
  }
  .discount-code {
    position: absolute;
    left: 126px; top: 975px;
    font-size: 40px;
    line-height: 1;
    color: var(--ink);
    white-space: nowrap;
  }
  .footer-band {
    position: absolute;
    left: 0; top: 1100px;
    width: 851px; height: 100px;
    background: var(--orange-deep);
  }
  .web-address {
    position: absolute;
    left: 68px; top: 16px;
    font-size: 47px;
    line-height: 1;
    color: var(--white);
    white-space: nowrap;
  }
</style>
</head>
<body>
<main class="flyer">
  <svg class="backdrop" width="851" height="1200" viewBox="0 0 851 1200">
    <defs>
      <linearGradient id="photoTone" x1="0" y1="0" x2="1" y2="1">
        <stop offset="0" stop-color="#3f2520"/>
        <stop offset="0.45" stop-color="#7a4a38"/>
        <stop offset="1" stop-color="#b07452"/>
      </linearGradient>
      <linearGradient id="sideGlow" x1="0" y1="0" x2="0" y2="1">
        <stop offset="0" stop-color="#c8462e"/>
        <stop offset="1" stop-color="#ef6a3a"/>
      </linearGradient>
    </defs>
    <rect class="side-glow" x="771" y="0" width="80" height="524" fill="url(#sideGlow)"/>
    <polygon class="hero-photo" points="0,0 771,0 771,524 0,634" fill="url(#photoTone)"
      role="img" aria-label="Warm-toned close-up photo of a musician playing an acoustic guitar"/>
  </svg>

  <div class="brand"><span class="brand-dot"></span>Ridgeline Guitars</div>

  <div class="offer-frame"></div>

  <div class="tag-backing"></div>
  <div class="tag">
    <p class="tag-lead">Get you first order</p>
    <p class="tag-value">20% discount</p>
  </div>
  <div class="tag-hole"></div>

  <div class="code-wash"></div>
  <p class="discount-code">Discount code: ABFF36D5</p>

  <footer class="footer-band">
    <p class="web-address">ridgelineguitars.co.uk</p>
  </footer>
</main>
</body>
</html>
```